Corvath Partners is a boutique consultancy focused on CXO-level advisory on strategy, operations, and organization in the Consumer Packaged Goods and Retail sector.

Our typical clients are senior level executives (Typically SVP level or higher), who hire us to help solve strategic business challenges. Our consultants are typically charged out at very high rates (Typically $2,000 - $3,000 per day), therefore, our business cards need to convey a high end, classy, yet professional image, consistent with high value strategic consulting.

We would like to see designs and colors that convey excellence, competence, and growth.

Our name 'Corvath' is derived from the Native American name of Mt. McKinley, the highest peak in North America. We would like to have a logo on our business card, that is simple yet conveys the aspirational nature of what we offer, i.e enabling the achievement of high performance.

Boutique

Corvath Partners, LLC
4718 Brennock Avenue Northwest, Suite 640
Washington, District of Columbia, 20093
United States
Mobile: +1 202 555 0143
elira.voss@corvathpartnersllc.com

```html
<!DOCTYPE html>
<html lang="en">
<head>
<meta charset="utf-8">
<title>Corvath Partners, LLC — Business Card</title>
<link rel="stylesheet" href="https://fonts.googleapis.com/css2?family=Cinzel:wght@500&family=Open+Sans:wght@400;600;700&display=swap">
<style>
  :root {
    --backdrop: #e9e9ea;
    --card: #f7f7f7;
    --brand-blue: #1b4a8c;
    --brand-navy: #14336a;
    --ink: #1f2328;
    --rule: #1b4a8c;
  }
  * { margin: 0; padding: 0; box-sizing: border-box; }
  html, body {
    width: 1200px;
    height: 800px;
    overflow: hidden;
    background: var(--backdrop);
  }
  .canvas {
    width: 1200px;
    height: 800px;
    display: flex;
    align-items: center;
    justify-content: center;
  }
  .card {
    position: relative;
    width: 840px;
    height: 480px;
    background: var(--card);
    box-shadow: 0 10px 30px rgba(0,0,0,0.12);
    font-family: "Open Sans", Arial, sans-serif;
    color: var(--ink);
  }
  .brand {
    position: absolute;
    top: 96px;
    right: 64px;
    display: flex;
    align-items: center;
    gap: 12px;
  }
  .brand-square {
    width: 18px;
    height: 18px;
    background: var(--brand-blue);
  }
  .brand-name {
    font-family: "Open Sans", Arial, sans-serif;
    font-weight: 600;
    font-size: 30px;
    letter-spacing: 0.5px;
    color: var(--brand-blue);
  }
  .holder {
    position: absolute;
    top: 168px;
    left: 64px;
  }
  .holder-name {
    font-family: "Cinzel", "Times New Roman", serif;
    font-weight: 500;
    font-size: 30px;
    color: var(--brand-navy);
    letter-spacing: 0.5px;
  }
  .holder-title {
    margin-top: 4px;
    padding-left: 12px;
    font-weight: 700;
    font-size: 14px;
    letter-spacing: 0.6px;
    text-transform: uppercase;
    color: var(--ink);
  }
  .office {
    position: absolute;
    top: 268px;
    left: 520px;
    padding-left: 22px;
    border-left: 2px solid var(--rule);
    font-size: 17px;
    line-height: 27px;
    color: var(--ink);
  }
  .office-name {
    font-weight: 700;
    color: var(--brand-blue);
  }
  .office-line { padding-left: 14px; }
  .contacts {
    position: absolute;
    left: 64px;
    bottom: 54px;
    list-style: none;
    font-size: 18px;
    line-height: 30px;
  }
  .contact {
    display: flex;
    align-items: center;
    gap: 12px;
  }
  .contact-icon {
    width: 20px;
    height: 20px;
    flex: none;
  }
</style>
</head>
<body>
<main class="canvas">
  <article class="card">
    <div class="brand">
      <span class="brand-square"></span>
      <span class="brand-name">Corvath Partners, LLC</span>
    </div>

    <div class="holder">
      <h1 class="holder-name">Daren Holloway</h1>
      <p class="holder-title">Director</p>
    </div>

    <address class="office" style="font-style: normal;">
      <div class="office-name">Corvath Partners, LLC</div>
      <div class="office-line">4718 Brennock Avenue Northwest</div>
      <div class="office-line">Suite 640 Washington</div>
      <div class="office-line">District of Columbia</div>
      <div class="office-line">20093 United States</div>
    </address>

    <ul class="contacts">
      <li class="contact">
        <svg class="contact-icon" viewBox="0 0 20 20" aria-hidden="true">
          <rect width="20" height="20" rx="3" fill="#1b4a8c"/>
          <path d="M6 4.5l2 .3.8 2.6-1.3 1a7 7 0 0 0 3.8 3.8l1-1.3 2.6.8.3 2c-.2.6-.8 1-1.5 1A9.5 9.5 0 0 1 5 6c0-.7.4-1.3 1-1.5z" fill="#fff"/>
        </svg>
        <span>+1 202 555 0143</span>
      </li>
      <li class="contact">
        <svg class="contact-icon" viewBox="0 0 20 20" aria-hidden="true">
          <rect width="20" height="20" rx="3" fill="#1b4a8c"/>
          <rect x="4" y="6" width="12" height="8" fill="#fff"/>
          <path d="M4 6l6 4.5L16 6" fill="none" stroke="#1b4a8c" stroke-width="1.2"/>
        </svg>
        <span>elira.voss@corvathpartnersllc.com</span>
      </li>
      <li class="contact">
        <svg class="contact-icon" viewBox="0 0 20 20" aria-hidden="true">
          <rect width="20" height="20" rx="3" fill="#1b4a8c"/>
          <g fill="none" stroke="#fff" stroke-width="1.1">
            <circle cx="10" cy="10" r="6"/>
            <ellipse cx="10" cy="10" rx="2.6" ry="6"/>
            <path d="M4 10h12M5 7h10M5 13h10"/>
          </g>
        </svg>
        <span>www.corvathpartnersllc.com</span>
      </li>
    </ul>
  </article>
</main>
</body>
</html>
```